Creative Business Card for my Sail Boat.. Tide & Time

Going to order PLASTIC business cards for my boat.. she is a sailing vessel catamaran named Tide & Time..

Target Market(s)

to impress other boaters with a unique designed plastic card

Contact Information for Business Card

S/V Tide & Time
Captain Owen Hartley
hartley@owen.example
Mobile/WhatsApp 1-555-318-7062
www.sailtideandtime.example

Requirements
Must have
• Cool colors. logo.. and info in Business Card Details.. Thanks! Utilize clear or cloudy plastic in design. Thanks

```html
<!DOCTYPE html>
<html lang="en">
<head>
<meta charset="utf-8">
<title>Tide &amp; Time – Business Card</title>
<link rel="stylesheet" href="https://fonts.googleapis.com/css2?family=Arimo:ital,wght@0,400;0,700;1,700&display=swap">
<style>
  :root {
    --backdrop: #2c333c;
    --card-brown: #4a2317;
    --card-edge: #3a1a10;
    --cream: #d9ccbc;
    --accent-green: #1f9a3c;
  }
  html, body {
    margin: 0;
    padding: 0;
    width: 1200px;
    height: 900px;
    overflow: hidden;
    background: var(--backdrop);
    font-family: "Arimo", Arial, sans-serif;
  }
  .canvas {
    position: relative;
    width: 1200px;
    height: 900px;
    display: flex;
    align-items: center;
    justify-content: center;
  }
  .business-card {
    position: relative;
    width: 1000px;
    height: 572px;
    background: var(--card-brown);
    border-radius: 14px;
    box-shadow: 0 0 0 2px var(--card-edge);
    color: var(--cream);
    overflow: hidden;
  }
  .brand-mark {
    position: absolute;
    left: 330px;
    top: 30px;
    width: 620px;
    height: 300px;
  }
  .brand-name {
    margin: 0;
    font-weight: 700;
    font-size: 128px;
    line-height: 0.95;
    letter-spacing: -2px;
    color: var(--cream);
  }
  .brand-name .line-two {
    display: block;
    padding-left: 150px;
  }
  .brand-dot {
    position: absolute;
    left: 488px;
    top: 150px;
    width: 96px;
    height: 96px;
    border-radius: 50%;
    border: 12px solid var(--accent-green);
    box-sizing: border-box;
  }
  .vessel {
    position: absolute;
    left: 56px;
    top: 370px;
  }
  .vessel-name {
    margin: 0;
    font-weight: 700;
    font-style: italic;
    font-size: 40px;
    letter-spacing: 0.5px;
  }
  .captain {
    margin: 8px 0 0;
    font-weight: 400;
    font-size: 30px;
  }
  .contact-list {
    position: absolute;
    left: 430px;
    top: 392px;
    margin: 0;
    padding: 0;
    list-style: none;
    font-weight: 700;
    font-size: 31px;
  }
  .contact-item {
    display: flex;
    align-items: center;
    gap: 14px;
    height: 52px;
  }
  .contact-icon {
    width: 30px;
    height: 30px;
    flex: none;
  }
  .icon-pair {
    display: flex;
    gap: 6px;
  }
  .chat-dot {
    width: 24px;
    height: 24px;
    border-radius: 50%;
    background: var(--cream);
    flex: none;
    align-self: center;
  }
</style>
</head>
<body>
<main class="canvas">
  <section class="business-card">
    <div class="brand-mark">
      <h1 class="brand-name">Tide &amp;<span class="line-two">Time</span></h1>
      <span class="brand-dot" aria-hidden="true"></span>
    </div>

    <div class="vessel">
      <p class="vessel-name">S/V Tide &amp; Time</p>
      <p class="captain">Captain Owen Hartley</p>
    </div>

    <ul class="contact-list">
      <li class="contact-item">
        <span class="icon-pair">
          <svg class="contact-icon" viewBox="0 0 30 30" aria-hidden="true">
            <rect x="2" y="2" width="26" height="26" rx="5" fill="var(--cream)"/>
            <path d="M10 7 l3 0 l1.5 5 l-2.5 1.5 q1.5 4 5 5.5 l1.5 -2.5 l5 1.5 l0 3 q-1 2 -4 2 q-11 -3 -12 -13 q0 -3 2.5 -3z" fill="var(--card-brown)"/>
          </svg>
          <span class="chat-dot" aria-hidden="true"></span>
        </span>
        <span>hartley@owen.example</span>
      </li>
      <li class="contact-item">
        <svg class="contact-icon" viewBox="0 0 30 30" aria-hidden="true">
          <rect x="2" y="6" width="26" height="18" rx="2" fill="var(--cream)"/>
          <path d="M3 8 L15 17 L27 8" fill="none" stroke="var(--card-brown)" stroke-width="2"/>
        </svg>
        <span>1-555-318-7062</span>
      </li>
      <li class="contact-item">
        <svg class="contact-icon" viewBox="0 0 30 30" aria-hidden="true">
          <g fill="none" stroke="var(--cream)" stroke-width="2">
            <circle cx="15" cy="15" r="12"/>
            <ellipse cx="15" cy="15" rx="5.5" ry="12"/>
            <line x1="3" y1="15" x2="27" y2="15"/>
            <line x1="5" y1="9" x2="25" y2="9"/>
            <line x1="5" y1="21" x2="25" y2="21"/>
          </g>
        </svg>
        <span>www.sailtideandtime.example</span>
      </li>
    </ul>
  </section>
</main>
</body>
</html>
```